Luxury Ayurvedic Hair Oil logo and package design

We need a logo and package design for our Ayurvedic and natural hair growth oil. Our company, Velmora, is the premier luxury Ayurvedic beauty brand, bringing ancient East-Indian natural and botanic health and beauty products to the US market. Our first major product - Velmora Hair Growth Oil - is a coconut oil based product that was developed by tribes in the Southern State of Kerala that includes ancient herbs like Gooseberry, Indigo, Indian Aloe, Balloon Vine and Brahmi.

The design should be catered to the high-end luxury market (minimal design, minimal text, fonts that invoke a sense of luxury). The primary colors should be deep blue for the packaging and gold for the characters (it's in the name - Velmora). We are looking to sell our products in Brenvale and Tolland Pryce and require packaging that is in line with products sold at these high-end retailers.

The final logo design and packaging should communicate luxury and the ancient wisdom of far-eastern traditions.

Target Market(s)

Velmora's main target is women who value fashionable/quality skincare, beauty, and fragrance products and are open to a medium to high price range. These women love uniqueness in brand and products that cannot be found elsewhere. They are looking for the next new "it" item that will take their haircare and beauty regiment to the next level.

Industry/Entity Type

Hair And Beauty

Font styles to use
Serif

Colors
2f73b3
ffc214

Requirements
Must have
• Must use deep blue (royal blue) background and gold text (to align with brand name). Must use luxurious fonts
Nice to have
• Flowers or other natural symbols, pictures that blend well with the product theme

```html
<!DOCTYPE html>
<html lang="en">
<head>
<meta charset="utf-8">
<title>Velmora Hair Growth Oil – Carton Dieline</title>
<link href="https://fonts.googleapis.com/css2?family=Cinzel:wght@400;500&family=Montserrat:wght@500;600;700&display=swap" rel="stylesheet">
<style>
  :root {
    --navy: #03344f;
    --navy-pattern: #0a3f5c;
    --gold: #d9a93a;
    --paper: #ffffff;
    --white-text: #f2f2f2;
  }
  html, body {
    margin: 0;
    padding: 0;
    width: 1200px;
    height: 858px;
    overflow: hidden;
    background: var(--paper);
  }
  .canvas {
    position: relative;
    width: 1200px;
    height: 858px;
  }
  .dieline {
    position: absolute;
    left: 0;
    top: 0;
  }
  .board { fill: var(--navy); }
  .botanical-pattern { fill: var(--navy-pattern); }
  .panel-edge { stroke: var(--paper); stroke-width: 1.4; fill: none; }

  .wordmark {
    position: absolute;
    writing-mode: vertical-rl;
    font-family: "Cinzel", serif;
    font-weight: 400;
    color: var(--gold);
    line-height: 1;
    white-space: nowrap;
  }
  .wordmark--standalone { left: 232px; top: 246px; font-size: 52px; letter-spacing: 2px; }
  .wordmark--front { left: 666px; top: 282px; font-size: 50px; letter-spacing: 0; }
  .wordmark--back { left: 1013px; top: 283px; font-size: 35px; letter-spacing: 0; }

  .brand-mark {
    position: absolute;
    display: flex;
    align-items: center;
    gap: 5px;
    font-family: "Cinzel", serif;
    font-weight: 500;
    color: var(--gold);
    white-space: nowrap;
  }
  .brand-mark__dot {
    display: inline-block;
    border-radius: 50%;
    background: var(--gold);
  }
  .brand-mark--standalone { left: 82px; top: 368px; font-size: 19px; }
  .brand-mark--standalone .brand-mark__dot { width: 12px; height: 12px; }
  .brand-mark--side { font-size: 12px; }
  .brand-mark--side .brand-mark__dot { width: 7px; height: 7px; }
  .brand-mark--left { left: 420px; top: 415px; }
  .brand-mark--right { left: 761px; top: 415px; }

  .product-name {
    position: absolute;
    left: 548px;
    top: 453px;
    width: 101px;
    margin: 0;
    text-align: right;
    font-family: "Montserrat", sans-serif;
    font-weight: 600;
    font-size: 12.5px;
    line-height: 14px;
    letter-spacing: 1.4px;
    color: var(--gold);
  }
  .ingredients {
    position: absolute;
    left: 548px;
    top: 512px;
    width: 100px;
    margin: 0;
    padding: 0;
    list-style: none;
    text-align: right;
    font-family: "Montserrat", sans-serif;
    font-weight: 600;
    font-size: 7px;
    line-height: 10.8px;
    letter-spacing: 0.9px;
    color: var(--gold);
  }

  .back-copy {
    position: absolute;
    left: 900px;
    width: 105px;
    margin: 0;
    text-align: right;
    font-family: "Montserrat", sans-serif;
    font-weight: 700;
    font-size: 7px;
    line-height: 10.8px;
    letter-spacing: 0.9px;
    color: var(--gold);
    text-transform: uppercase;
  }
  .back-copy--story { top: 283px; }
  .back-copy--detail { top: 347px; }
  .back-rule {
    position: absolute;
    left: 913px;
    top: 341px;
    width: 92px;
    height: 1px;
    background: var(--gold);
  }
  .volume {
    position: absolute;
    left: 956px;
    top: 452px;
    font-family: "Montserrat", sans-serif;
    font-weight: 500;
    font-size: 11px;
    color: var(--white-text);
  }
</style>
</head>
<body>
<main class="canvas">
  <svg class="dieline" width="1200" height="858" viewBox="0 0 1200 858" xmlns="http://www.w3.org/2000/svg">
    <!-- standalone front face -->
    <rect class="board" x="37" y="228" width="267" height="297"/>

    <!-- top lid flap and lid -->
    <polygon class="board" points="561,35 706,35 718,94 549,94"/>
    <rect class="botanical-pattern" x="549" y="94" width="169" height="166" role="img" aria-label="Botanical line pattern of coconuts, flowers, aloe and leaves"/>

    <!-- dust flaps above side panels -->
    <polygon class="board" points="393,217 533,217 547,262 378,262"/>
    <polygon class="board" points="733,217 873,217 888,262 719,262"/>
    <polygon class="board" points="904,217 1044,217 1059,262 889,262"/>

    <!-- main panels -->
    <rect class="botanical-pattern" x="378" y="262" width="169" height="314" role="img" aria-label="Botanical line pattern of coconuts, flowers, aloe and leaves"/>
    <rect class="botanical-pattern" x="549" y="262" width="169" height="314" role="img" aria-label="Botanical line pattern of coconuts, flowers, aloe and leaves"/>
    <rect class="botanical-pattern" x="719" y="262" width="169" height="314" role="img" aria-label="Botanical line pattern of coconuts, flowers, aloe and leaves"/>
    <rect class="board" x="889" y="262" width="170" height="314"/>

    <!-- glue tab -->
    <polygon class="board" points="1059,264 1112,277 1112,563 1059,576"/>

    <!-- dust flaps below side panels -->
    <polygon class="board" points="378,577 547,577 533,623 393,623"/>
    <polygon class="board" points="719,577 888,577 873,623 733,623"/>
    <polygon class="board" points="889,577 1059,577 1044,623 904,623"/>

    <!-- base and tuck flap -->
    <rect class="board" x="549" y="580" width="169" height="166"/>
    <polygon class="board" points="549,746 718,746 705,803 562,803"/>

    <!-- crease lines -->
    <line class="panel-edge" x1="548" y1="262" x2="548" y2="576"/>
    <line class="panel-edge" x1="718.5" y1="262" x2="718.5" y2="576"/>
    <line class="panel-edge" x1="888.5" y1="262" x2="888.5" y2="576"/>
    <line class="panel-edge" x1="1059" y1="262" x2="1059" y2="576"/>
    <line class="panel-edge" x1="378" y1="262" x2="1059" y2="262"/>
    <line class="panel-edge" x1="378" y1="577" x2="1059" y2="577"/>
    <line class="panel-edge" x1="549" y1="94" x2="718" y2="94"/>
    <line class="panel-edge" x1="549" y1="746" x2="718" y2="746"/>
  </svg>

  <!-- standalone front -->
  <div class="brand-mark brand-mark--standalone"><span class="brand-mark__dot"></span>VELMORA</div>
  <div class="wordmark wordmark--standalone">VELMORA</div>

  <!-- side panels -->
  <div class="brand-mark brand-mark--side brand-mark--left"><span class="brand-mark__dot"></span>VELMORA</div>
  <div class="brand-mark brand-mark--side brand-mark--right"><span class="brand-mark__dot"></span>VELMORA</div>

  <!-- front panel -->
  <div class="wordmark wordmark--front">VELMORA</div>
  <h1 class="product-name">AYURVEDIC HAIR GROWTH ~OIL~</h1>
  <ul class="ingredients">
    <li>COCONUT OIL</li>
    <li>GOOSEBERRY</li>
    <li>INDIAN ALOE</li>
    <li>BALLOON VINE</li>
    <li>&amp; BRAHMI</li>
  </ul>

  <!-- back panel -->
  <p class="back-copy back-copy--story">Our products are inspired by ancient treatments dating back hundreds of years.</p>
  <div class="back-rule"></div>
  <p class="back-copy back-copy--detail">Some further text to better describe the product will be placed here.</p>
  <div class="volume">100ml</div>
  <div class="wordmark wordmark--back">VELMORA</div>
</main>
</body>
</html>
```